Full service residential and commercial painting
Finest quality attention to detail
All workmanship guaranteed
Email :norabvantreel@mailbox-example.fr
Mobile: 0417382650
Industry/Entity Type
Residential
Contact Information for Business Card
Henri marsot painting & decorating
Requirements
Nice to have
- Am thinking about someone can be painting my name on the card with HM painting with the logos of brush,pot tray and roller sleeves

```html
<!DOCTYPE html>
<html lang="en">
<head>
<meta charset="utf-8">
<title>Henri Marsot Painting &amp; Decorating — Business Card</title>
<link rel="stylesheet" href="https://fonts.googleapis.com/css2?family=Marcellus&family=Arimo&display=swap">
<style>
  :root {
    --backdrop: #5a5a5a;
    --backdrop-light: #8a8a8a;
    --card: #ffffff;
    --teal: #3aa3b8;
    --green-light: #d4e24a;
    --green: #8fcb3f;
    --green-deep: #78bb3a;
    --white: #ffffff;
  }
  * { box-sizing: border-box; margin: 0; padding: 0; }
  html, body { width: 1200px; height: 900px; overflow: hidden; }
  body {
    background: radial-gradient(ellipse at 50% 40%, var(--backdrop-light), var(--backdrop) 75%);
    position: relative;
  }
  .card {
    position: absolute;
    left: 75px; top: 150px;
    width: 1050px; height: 600px;
    background: var(--card);
    box-shadow: 0 18px 40px rgba(0,0,0,.35);
    overflow: hidden;
  }
  .services {
    position: absolute;
    left: 80px; top: 62px;
    font-family: "Arimo", Arial, sans-serif;
    font-size: 24px;
    line-height: 34px;
    letter-spacing: 2px;
    color: var(--teal);
    list-style: none;
    white-space: nowrap;
  }
  .logo-art {
    position: absolute;
    left: 680px; top: 36px;
    width: 290px; height: 160px;
    border-radius: 8px;
    background: linear-gradient(120deg, #4bb4c8 0%, #e3a43a 45%, #cfe9ec 100%);
  }
  .brand {
    position: absolute;
    left: 610px; top: 210px;
    width: 420px;
    text-align: center;
    font-family: "Marcellus", serif;
    font-weight: 400;
    color: var(--teal);
    white-space: nowrap;
  }
  .brand-name { font-size: 42px; letter-spacing: 4px; line-height: 1; }
  .brand-trade { font-size: 18px; letter-spacing: 4px; margin-top: 8px; }
  .paint-band {
    position: absolute;
    left: 0; top: 320px;
    width: 1050px; height: 150px;
  }
  .brush-art {
    position: absolute;
    left: 60px; top: 250px;
    width: 230px; height: 230px;
    border-radius: 10px;
    background: linear-gradient(150deg, #e9a844 0%, #3a3a3a 55%, #a9d442 100%);
  }
  .contact {
    position: absolute;
    left: 420px; top: 348px;
    font-family: "Marcellus", serif;
    font-size: 21px;
    line-height: 44px;
    letter-spacing: 2px;
    color: var(--white);
    list-style: none;
    white-space: nowrap;
  }
</style>
</head>
<body>
  <section class="card">
    <ul class="services">
      <li>Full service residential</li>
      <li>and commercial painting</li>
      <li>Finest quality attention to detail</li>
      <li>All workmanship guaranteed</li>
    </ul>

    <div class="logo-art" role="img" aria-label="Illustration of a paintbrush dripping teal paint crossed with a paint roller"></div>

    <div class="brand">
      <div class="brand-name">HENRI MARSOT</div>
      <div class="brand-trade">PAINTING &amp; DECORATING</div>
    </div>

    <svg class="paint-band" viewBox="0 0 1050 150" aria-hidden="true">
      <defs>
        <linearGradient id="band-fill" x1="0" y1="0" x2="1" y2="0">
          <stop offset="0" stop-color="#d4e24a"/>
          <stop offset="0.55" stop-color="#8fcb3f"/>
          <stop offset="1" stop-color="#78bb3a"/>
        </linearGradient>
      </defs>
      <path d="M230 20 L1050 0 L1050 130 L260 150 Q240 120 250 90 Q225 60 230 20 Z" fill="url(#band-fill)"/>
    </svg>

    <div class="brush-art" role="img" aria-label="Illustration of a wooden paintbrush laying down a green paint stroke"></div>

    <ul class="contact">
      <li>email :norabvantreel@mailbox-example.fr</li>
      <li>mobile: 0417382650</li>
    </ul>
  </section>
</body>
</html>
```